Velmora Water Purification

We need a website set up on a "Free account" WordPress platform. (This is the type of Wordpress site that you can sign up for and create online for free (not a server-hosted type.)
The website will be for a water purification company. They install devices in homes to purify the water for safer drinking, bathing, and cleaning.
Our logo is attached. Please keep color scheme of the website consistent with the logo.
Water Purification

```html
<!DOCTYPE html>
<html lang="en">
<head>
<meta charset="utf-8">
<title>Velmora Water Purification</title>
<link href="https://fonts.googleapis.com/css2?family=Montserrat:wght@400;500;600;700&family=Raleway:ital,wght@0,400;0,600;0,700;1,400&display=swap" rel="stylesheet">
<style>
:root{
  --blue:#2d86c0;
  --blue-dark:#1f6fa3;
  --cyan:#1bb0e0;
  --deep:#0b4a68;
  --ink:#222;
  --text:#666;
  --muted:#999;
  --line:#e3e3e3;
  --grey-bg:#f5f5f5;
  --footer:#2b2c2f;
  --white:#fff;
}
*{box-sizing:border-box;margin:0;padding:0}
html,body{width:1200px;height:3279px;overflow:hidden}
body{font-family:"Raleway",sans-serif;color:var(--text);background:var(--white);position:relative}
.abs{position:absolute}
.btn{position:absolute;display:flex;align-items:center;justify-content:center;font:500 14px "Montserrat",sans-serif;letter-spacing:.5px;text-transform:uppercase}
.btn-blue{background:var(--blue);color:var(--white)}
.eyebrow{font:italic 400 13px "Raleway",sans-serif;color:var(--ink)}
.heading{font:700 27px "Montserrat",sans-serif;color:var(--ink)}
.rule{height:2px;width:62px;background:#333}
.para{font-size:14px;line-height:19px;color:var(--text)}

.topbar{left:0;top:0;width:1200px;height:35px;background:#f4f4f4;border-bottom:1px solid #e6e6e6;font:400 11px "Montserrat",sans-serif;color:#555}
.topbar .item{position:absolute;top:11px;display:flex;align-items:center;gap:7px}
.social-mini{position:absolute;top:12px;width:11px;height:11px;border-radius:2px;background:var(--blue)}

.nav{left:0;top:35px;width:1200px;height:75px;background:var(--white)}
.brand{position:absolute;left:118px;top:20px;display:flex;align-items:center;gap:9px;font:700 20px "Raleway",sans-serif;color:var(--blue)}
.brand .dot{width:34px;height:34px;border-radius:50%;background:var(--blue)}
.menu{position:absolute;top:29px;font:600 12px "Montserrat",sans-serif;color:#333;letter-spacing:.2px;white-space:nowrap}

.hero{left:0;top:110px;width:1200px;height:445px;background:radial-gradient(ellipse at 72% 40%,#7fe3fb 0%,#2bbfe8 30%,#0d8cbc 62%,#06506f 100%)}
.hero h1{position:absolute;left:100px;top:100px;width:600px;font:700 38px/50px "Raleway",sans-serif;color:var(--white)}
.hero p{position:absolute;left:100px;top:210px;width:560px;font-size:13px;line-height:18px;color:#e8f8ff}
.btn-white{left:102px;top:298px;width:168px;height:48px;background:var(--white);color:var(--blue)}

.photo-glass{left:630px;top:625px;width:318px;height:218px;background:linear-gradient(135deg,#d9efe0,#8cc96a 55%,#4a9b3c)}
.photo-shower{left:775px;top:727px;width:315px;height:218px;background:linear-gradient(135deg,#2a3d4b,#0e1820 60%,#33495a)}

.services{left:0;top:1058px;width:1200px;height:538px;background:var(--grey-bg)}
.card{position:absolute;top:180px;width:250px;height:217px;background:var(--white);border:1px solid var(--line);text-align:center}
.card .icon{width:50px;height:50px;margin:41px auto 0;background:var(--blue);display:flex;align-items:center;justify-content:center}
.card h3{margin-top:19px;font:700 14px "Montserrat",sans-serif;color:var(--ink)}
.card p{margin:6px 20px 0;font-size:13px;line-height:17px;color:#555}

.product{position:absolute;top:1775px;width:309px;height:207px;background:linear-gradient(90deg,#bfe6f6,#eef9fd 45%,#8fd2ef)}
.product-name{position:absolute;top:1995px;font:700 13px "Montserrat",sans-serif;color:var(--ink)}
.view{left:536px;top:1865px;width:138px;height:40px;background:var(--white);color:#222;font:600 13px "Montserrat",sans-serif;box-shadow:0 2px 6px rgba(0,0,0,.2);text-transform:none}
.dotc{position:absolute;top:2088px;width:7px;height:7px;border-radius:50%;background:#bbb}

.why{left:0;top:2138px;width:1200px;height:420px;background:linear-gradient(90deg,#6f7a7c 0%,#8b9697 45%,#cbbfb2 70%,#b59a82 100%)}
.why .eyebrow,.why .heading{color:var(--white)}
.why .para{color:#f1f1f1;width:490px}

.quote{left:112px;top:2720px;font:700 48px/1 Georgia,serif;color:#333}
.logos{left:590px;top:2655px;width:514px;height:190px}
.logo-cell{position:absolute;width:171px;height:95px;display:flex;align-items:center;justify-content:center;font:600 16px "Montserrat",sans-serif;color:#888}

.footer{left:0;top:2920px;width:1200px;height:359px;background:var(--footer);color:#ddd}
.footer h4{position:absolute;top:78px;font:700 18px "Montserrat",sans-serif;color:var(--white)}
.f-label{position:absolute;font:700 12px "Montserrat",sans-serif;color:var(--white)}
.f-val{position:absolute;font:500 12px "Montserrat",sans-serif;color:var(--white)}
.field{position:absolute;left:787px;width:305px;height:42px;border:1px solid #777;font:400 12px "Montserrat",sans-serif;color:#ccc;padding:12px 8px}
.f-social{position:absolute;top:268px;width:22px;height:22px;border-radius:3px;background:#cfcfcf}
</style>
</head>
<body>

<header class="abs topbar">
  <div class="item" style="left:160px">
    <svg width="12" height="12" viewBox="0 0 24 24"><path fill="#2d86c0" d="M6.6 10.8a15 15 0 0 0 6.6 6.6l2.2-2.2c.3-.3.7-.4 1-.2 1.1.4 2.3.6 3.6.6.6 0 1 .4 1 1V20c0 .6-.4 1-1 1A17 17 0 0 1 3 4c0-.6.4-1 1-1h3.5c.6 0 1 .4 1 1 0 1.3.2 2.5.6 3.6.1.3 0 .7-.2 1z"/></svg>
    (+101) 555.0147
  </div>
  <div class="item" style="left:322px">
    <svg width="13" height="10" viewBox="0 0 26 20"><rect x="1" y="1" width="24" height="18" fill="none" stroke="#2d86c0" stroke-width="2"/><path d="M1 1l12 10L25 1" fill="none" stroke="#2d86c0" stroke-width="2"/></svg>
    info@velmora.com
  </div>
  <span class="social-mini" style="left:820px"></span>
  <span class="social-mini" style="left:852px"></span>
  <span class="social-mini" style="left:884px"></span>
  <span class="social-mini" style="left:918px"></span>
  <div class="item" style="left:972px">
    <svg width="13" height="10" viewBox="0 0 26 20"><rect x="1" y="1" width="24" height="18" fill="none" stroke="#777" stroke-width="2"/><path d="M1 1l12 10L25 1" fill="none" stroke="#777" stroke-width="2"/></svg>
    Send a Message
  </div>
</header>

<nav class="abs nav">
  <div class="brand"><span class="dot"></span>Velmora</div>
  <span class="menu" style="left:316px">UNDERSINK SYSTEM</span>
  <span class="menu" style="left:488px">SINKTOP SYSTEM</span>
  <span class="menu" style="left:638px">WHOLE HOUSE SYSTEM ˅</span>
  <span class="menu" style="left:823px">REPLACEMENT FILTERS ˅</span>
  <svg class="abs" style="left:1030px;top:29px" width="13" height="13" viewBox="0 0 24 24"><circle cx="10" cy="10" r="7" fill="none" stroke="#333" stroke-width="3"/><path d="M15 15l7 7" stroke="#333" stroke-width="3"/></svg>
  <svg class="abs" style="left:1066px;top:28px" width="13" height="14" viewBox="0 0 24 26"><circle cx="12" cy="7" r="6" fill="#333"/><path d="M1 26c0-7 5-11 11-11s11 4 11 11z" fill="#333"/></svg>
</nav>

<section class="abs hero" role="img" aria-label="Splashing water with air bubbles on a bright blue background">
  <h1>THE BEST PURIFICATION SYSTEMS</h1>
  <p>Lorem ipsum dolor sit amet, consectetur adipisicing elit, sed do eiusmod tempor incididunt ut labore et dolore magna aliqua. Ut enim ad minim veniam, quis nostrud exercitation.</p>
  <span class="btn btn-white">Learn More</span>
</section>

<section class="about">
  <div class="abs eyebrow" style="left:98px;top:626px">We are Velmora</div>
  <h2 class="abs heading" style="left:98px;top:648px">We Birng something Special</h2>
  <p class="abs para" style="left:98px;top:712px;width:492px">Lorem ipsum dolor sit amet, consectetur adipisicing elit, sed do eiusmod tempor incididunt ut labore et dolore magna aliqua. Ut enim ad minim veniam, quis nostrud exercitation ullamco laboris nisi ut aliquip ex ea commodo consequat. Duis aute irure dolor in reprehenderit in voluptate velit esse cillum dolore eu fugiat nulla pariatur.</p>
  <p class="abs para" style="left:98px;top:817px;width:492px">Excepteur sint occaecat cupidatat non proident, sunt in culpa qui officia deserunt mollit anim id est laborum. Sed ut perspiciatis unde omnis iste natus error sit voluptatem accusantium doloremque laudantium.</p>
  <span class="btn btn-blue" style="left:98px;top:915px;width:150px;height:46px">Contact Us</span>
  <div class="abs photo-glass" role="img" aria-label="Glass of clear water against green leaves"></div>
  <div class="abs photo-shower" role="img" aria-label="Shower head spraying water on a dark background"></div>
</section>

<section class="abs services">
  <div class="abs eyebrow" style="left:0;width:1200px;text-align:center;top:70px">We are Velmora</div>
  <h2 class="abs heading" style="left:0;width:1200px;text-align:center;top:92px;font-size:25px">What We Do For You</h2>
  <div class="card" style="left:98px">
    <div class="icon"><svg width="28" height="22" viewBox="0 0 28 22"><path d="M2 4q3-3 6 0t6 0 6 0 6 0M2 11q3-3 6 0t6 0 6 0 6 0M2 18q3-3 6 0t6 0 6 0 6 0" fill="none" stroke="#fff" stroke-width="2"/></svg></div>
    <h3>Undersink Systems</h3>
    <p>Lorem ipsum dolor sit amet, consectetur adipisicing elit, sed do eiusmod tempor</p>
  </div>
  <div class="card" style="left:351px">
    <div class="icon"><svg width="24" height="24" viewBox="0 0 24 24"><path d="M2 3h20l-8 9v8l-4 2v-10z" fill="#fff"/></svg></div>
    <h3>sinktop Systems</h3>
    <p>Lorem ipsum dolor sit amet, consectetur adipisicing elit, sed do eiusmod tempor</p>
  </div>
  <div class="card" style="left:604px">
    <div class="icon"><svg width="18" height="26" viewBox="0 0 18 26"><path d="M9 1C6 8 1 12 1 17a8 8 0 0 0 16 0c0-5-5-9-8-16z" fill="#fff"/></svg></div>
    <h3>Whole Home Systems</h3>
    <p>Lorem ipsum dolor sit amet, consectetur adipisicing elit, sed do eiusmod tempor</p>
  </div>
  <div class="card" style="left:856px">
    <div class="icon"><svg width="28" height="28" viewBox="0 0 28 28"><rect x="4" y="10" width="14" height="16" fill="#fff"/><path d="M18 14l8-8" stroke="#fff" stroke-width="3"/><rect x="8" y="4" width="6" height="6" fill="#fff"/></svg></div>
    <h3>Garden &amp; Hydroponic</h3>
    <p>Lorem ipsum dolor sit amet, consectetur adipisicing elit, sed do eiusmod tempor</p>
  </div>
  <span class="btn btn-blue" style="left:520px;top:439px;width:160px;height:48px">Learn More</span>
</section>

<section class="products">
  <div class="abs eyebrow" style="left:112px;top:1664px">We are Velmora</div>
  <h2 class="abs heading" style="left:112px;top:1684px">Our Best Products</h2>
  <div class="abs rule" style="left:112px;top:1728px"></div>
  <div class="product" style="left:112px" role="img" aria-label="Three-stage home water filter unit"></div>
  <div class="product" style="left:446px" role="img" aria-label="Three-stage home water filter unit"></div>
  <div class="product" style="left:781px" role="img" aria-label="Three-stage home water filter unit"></div>
  <span class="btn view">View Details</span>
  <div class="product-name" style="left:112px">Home Water Filter</div>
  <div class="product-name" style="left:446px">Home Water Filter</div>
  <div class="product-name" style="left:781px">Home Water Filter</div>
  <span class="dotc" style="left:579px;background:#444"></span>
  <span class="dotc" style="left:596px"></span>
  <span class="dotc" style="left:613px"></span>
</section>

<section class="abs why" role="img" aria-label="Woman smiling while holding a glass of water">
  <div class="abs eyebrow" style="left:110px;top:65px">We are Velmora</div>
  <h2 class="abs heading" style="left:110px;top:86px">Why Velmora</h2>
  <p class="abs para" style="left:110px;top:130px">Lorem ipsum dolor sit amet, consectetur adipisicing elit, sed do eiusmod tempor incididunt ut labore et dolore magna aliqua. Ut enim ad minim veniam, quis nostrud exercitation ullamco laboris nisi ut aliquip ex ea commodo consequat.</p>
  <p class="abs para" style="left:110px;top:216px">Duis aute irure dolor in reprehenderit in voluptate velit esse cillum dolore eu fugiat nulla pariatur. Excepteur sint occaecat cupidatat non proident.</p>
  <span class="btn btn-blue" style="left:110px;top:303px;width:160px;height:46px">Learn More</span>
</section>

<section class="testimonial">
  <div class="abs eyebrow" style="left:112px;top:2620px">We are Velmora</div>
  <h2 class="abs heading" style="left:112px;top:2641px;font-size:25px">What Our Client Say</h2>
  <div class="abs rule" style="left:112px;top:2685px"></div>
  <div class="abs quote">“</div>
  <p class="abs para" style="left:145px;top:2730px;width:410px;font-style:italic;font-size:12px;line-height:16px;color:#777">Lorem ipsum dolor sit amet, consectetur adipisicing elit, sed do eiusmod tempor incididunt ut labore et dolore magna aliqua. Ut enim ad minim veniam, quis nostrud exercitation ullamco laboris nisi.</p>
  <div class="abs" style="left:145px;top:2806px;font:700 14px 'Montserrat',sans-serif;color:#222">Owen Marsh</div>
  <div class="abs" style="left:145px;top:2826px;font:italic 12px 'Raleway',sans-serif;color:#555">Leader</div>
  <div class="abs logos">
    <svg class="abs" width="514" height="190"><path d="M171 0v190M342 0v190M0 95h514" stroke="#e3e3e3"/></svg>
    <div class="logo-cell" style="left:0;top:0"><span style="border:1px solid #ccc;padding:18px 14px">Stonefield</span></div>
    <div class="logo-cell" style="left:171px;top:0">Norvik</div>
    <div class="logo-cell" style="left:342px;top:0">Halden</div>
    <div class="logo-cell" style="left:0;top:95px">Brightway</div>
    <div class="logo-cell" style="left:171px;top:95px">Tellbrook</div>
    <div class="logo-cell" style="left:342px;top:95px">Quorra</div>
  </div>
</section>

<footer class="abs footer">
  <div class="abs" style="left:112px;top:70px;display:flex;align-items:center;gap:9px;font:700 18px 'Raleway',sans-serif;color:#fff"><span style="width:30px;height:30px;border-radius:50%;background:var(--cyan)"></span>Velmora</div>
  <p class="abs" style="left:112px;top:170px;width:380px;font:500 12px/16px 'Raleway',sans-serif;color:#eee">Lorem ipsum dolor sit amet, consectetur adipisicing elit, sed do eiusmod tempor incididunt ut labore et dolore magna aliqua. Ut enim ad minim veniam, quis nostrud exercitation ullamco</p>
  <span class="f-social" style="left:112px"></span>
  <span class="f-social" style="left:158px"></span>
  <span class="f-social" style="left:204px"></span>
  <span class="f-social" style="left:250px"></span>
  <div class="abs" style="left:112px;top:315px;font:500 11px 'Montserrat',sans-serif;color:#ddd">Copyright 2017 Velmora. All Right Reserved.</div>

  <h4 style="left:480px">Contact Us</h4>
  <div class="abs" style="left:480px;top:106px;width:80px;height:2px;background:#fff"></div>
  <div class="f-label" style="left:480px;top:128px">ADDRESS:</div>
  <div class="f-val" style="left:480px;top:145px">Lark Ave, Ste 4 Fernhill, 480213</div>
  <div class="f-label" style="left:480px;top:188px">PHONE NUMBER:</div>
  <div class="f-val" style="left:480px;top:205px">(+101), 5550-318</div>
  <div class="f-label" style="left:480px;top:248px">EMAIL:</div>
  <div class="f-val" style="left:480px;top:265px">info@velmora.com</div>

  <h4 style="left:787px">Leave A Message</h4>
  <div class="abs" style="left:787px;top:106px;width:80px;height:2px;background:#fff"></div>
  <div class="field" style="top:122px">Full Name:</div>
  <div class="field" style="top:166px">Email:</div>
  <div class="field" style="top:210px">Phone:</div>
  <div class="field" style="top:254px;height:90px">Message:</div>
  <div class="abs" style="left:1052px;top:318px;width:36px;height:22px;background:#fff;display:flex;align-items:center;justify-content:center">
    <svg width="14" height="12" viewBox="0 0 14 12"><path d="M0 6l14-6-3 12-4-4z" fill="#2b2c2f"/></svg>
  </div>
</footer>

</body>
</html>
```